Banners for a bowtie/tie Fashion shop

I need banners (770x100) for a necktie and bowtie shop (http://www.kelorin.dk)

5 BOWTIE BANNERS:

I need the 3 text versions for eatch bowtie banner:

Danmarks største udvalg af butterfly
Køb butterfly. FRI fragt og FRI retur
Butterfly fra 199,- inkl. FRI fragt

5 NECKTIE BANNERS:

I need the 3 text versions for eatch necktie banner:

Danmarks største udvalg af slips
Køb slips. FRI fragt og FRI retur
Slips fra 199,- inkl. FRI fragt

All banners should contain the logo. All in JPG format and Photoshop/Inddesign/illustrator format

Target Market(s)

Guys and Gays

Industry/Entity Type

Shop

Requirements
Must have
• Logo
Nice to have
• Nice new pictures

```html
<!DOCTYPE html>
<html lang="da">
<head>
<meta charset="utf-8">
<title>Kelorin – Danmarks største udvalg af slips</title>
<link href="https://fonts.googleapis.com/css2?family=Special+Elite&family=Nunito:wght@600&display=swap" rel="stylesheet">
<style>
  :root {
    --curtain-light: #9a9793;
    --curtain-mid: #6f6c69;
    --curtain-dark: #4a4846;
    --band: rgba(30, 30, 30, 0.88);
    --headline: #ffffff;
    --accent: #1fc0ee;
    --corner: #ffffff;
    --logo-ink: #2b2b2b;
    --model-light: #8a7c73;
    --model-dark: #1f1d1e;
  }
  html, body {
    margin: 0;
    padding: 0;
    overflow: hidden;
    background: #ffffff;
  }
  .banner {
    position: relative;
    width: 1200px;
    height: 156px;
    overflow: hidden;
  }
  .banner__backdrop {
    position: absolute;
    inset: 0;
    background:
      repeating-linear-gradient(90deg, rgba(255,255,255,0.05) 0 14px, rgba(0,0,0,0.06) 14px 30px),
      linear-gradient(90deg, var(--curtain-dark) 0%, var(--curtain-light) 35%, var(--curtain-mid) 60%, var(--curtain-light) 100%);
  }
  .banner__model {
    position: absolute;
    left: 640px;
    top: 0;
    width: 370px;
    height: 156px;
    background: radial-gradient(ellipse at 50% 35%, var(--model-light) 0%, #5e534e 45%, var(--model-dark) 100%);
    opacity: 0.9;
  }
  .banner__band {
    position: absolute;
    left: 0;
    top: 31px;
    width: 678px;
    height: 52px;
    background: var(--band);
  }
  .banner__headline {
    position: absolute;
    left: 70px;
    top: 28px;
    margin: 0;
    font-family: "Special Elite", "Courier New", monospace;
    font-weight: 400;
    line-height: 1;
  }
  .headline__line {
    display: block;
    text-transform: uppercase;
    letter-spacing: 1px;
  }
  .headline__line--top {
    color: var(--headline);
    font-size: 46px;
  }
  .headline__line--bottom {
    color: var(--accent);
    font-size: 48px;
    margin-top: -6px;
  }
  .banner__corner {
    position: absolute;
    right: 0;
    bottom: 0;
    width: 200px;
    height: 156px;
  }
  .banner__logo {
    position: absolute;
    right: 24px;
    bottom: 14px;
    font-family: "Nunito", Arial, sans-serif;
    font-weight: 600;
    font-size: 30px;
    color: var(--logo-ink);
    letter-spacing: 0.5px;
  }
</style>
</head>
<body>
  <div class="banner">
    <div class="banner__backdrop" role="img" aria-label="Grå gardinbaggrund"></div>
    <div class="banner__model" role="img" aria-label="Mand i mørkt jakkesæt der retter på sin butterfly"></div>
    <div class="banner__band"></div>
    <h1 class="banner__headline">
      <span class="headline__line headline__line--top">Danmarks största</span>
      <span class="headline__line headline__line--bottom">Udvalg af slips</span>
    </h1>
    <svg class="banner__corner" viewBox="0 0 200 156" aria-hidden="true">
      <polygon points="200,28 200,156 22,156" fill="var(--corner)"/>
    </svg>
    <a class="banner__logo" href="http://www.kelorin.dk" style="text-decoration:none">kelorin</a>
  </div>
</body>
</html>
```